Church needs a graphic design/flyer layout for upcoming series

I need a multi-purpose design for promoting both our upcoming series of messages and our fall kick-off event where we will launch the messages.

Our promotion will be printed on a two-sided. One side is simple and focuses on the series and the other side has details in regards to the event. I have provided an attachment example of what we did last time.

The design needs to be multi-purpose because it will be used for our sermon Power Points, placed on our website banner, social media, etc.

• Sermon series is called “Harbor Lanterns”
• The subtitle will be “What’s keeping you from God?”
• Our name logo should be on the graphic as well.
• The subject manner will revolve around common hurdles that people face about God and Christianity: The existence of God, the exclusivity of religion, Hell, the reliability of the Bible, Hypocrisy in the church, etc.
• Our mission is “Connecting Young Families to Christ” so our focus is to reach out to families while not being exclusive to others.
• Our target audience is families with school-aged kids.
• This series is an invitational focus so we want it to be appealing to non-church goers.
• It should be attention grabbing while not being too ‘edgy’

• The front of the card will most likely consist the Sermon Series Graphic, title & subtitle of the series, and perhaps our name logo somewhere on it.
• The back of the card will invite and give the basic information for the event so that the people will be encouraged to save the date and come to the event.
• Here are some things that could be included on that advertisement:
o The name of the event: “Westbrook Commons Open Day”
o The date and time of the event: Sept 23rd @ 10:30
o Features of the event:
 Free lunch
 Children’s program
 Bouncy Castle
 Start of the “Harbor Lanterns” messages.
 Sample of topics
o Information about the church: our website and address, etc
o Engaging pictures and graphics.
• The rest of the tone and manner are the same as the sermon series graphic.
The flyer will be 11X14, like a postcard size.

Target Market(s)

Young families who are spiritually curious but not committed church attenders.

Colors

Designer to choose colors to be used in the design.

Requirements
Nice to have
• A modern and professional looking design.
Should not have
• Anything offensive or not family friendly.

```html
<!DOCTYPE html>
<html lang="en">
<head>
<meta charset="utf-8">
<title>Harbor Lanterns – Series Card</title>
<link rel="stylesheet" href="https://fonts.googleapis.com/css2?family=Playball&family=Satisfy&family=Alegreya:wght@400;700&family=Roboto+Condensed:wght@400&family=Crimson+Pro:wght@400;600;700&display=swap">
<style>
  :root {
    --stage: #7f7f7f;
    --navy: #0f3f8c;
    --navy-deep: #0a2d6a;
    --royal: #0a56a8;
    --sky: #0a6cc0;
    --orange: #f28c1c;
    --gold: #f6c31a;
    --purple: #7a2a86;
    --white: #ffffff;
    --photo-light: #e9d6b0;
    --photo-mid: #a7865b;
    --photo-dark: #3a2a1c;
  }
  * { margin: 0; padding: 0; box-sizing: border-box; }
  html, body { width: 800px; height: 1200px; overflow: hidden; }
  body { background: var(--stage); position: relative; }

  .card { position: absolute; left: 104px; width: 594px; height: 466px; overflow: hidden; }

  /* Front */
  .card-front {
    top: 90px;
    background: radial-gradient(ellipse at 50% 45%, #1a5bb0 0%, var(--navy) 55%, var(--navy-deep) 100%);
    color: var(--white);
  }
  .bracket { position: absolute; width: 86px; height: 86px; border-color: var(--white); border-style: solid; border-width: 0; }
  .bracket.tl { left: 20px; top: 20px; border-top-width: 2px; border-left-width: 2px; }
  .bracket.tr { right: 20px; top: 20px; border-top-width: 2px; border-right-width: 2px; }
  .bracket.bl { left: 20px; bottom: 20px; border-bottom-width: 2px; border-left-width: 2px; }
  .bracket.br { right: 20px; bottom: 20px; border-bottom-width: 2px; border-right-width: 2px; }

  .series-title {
    position: absolute; top: 40px; left: 0; width: 100%; text-align: center;
    font-family: "Playball", cursive; font-size: 66px; line-height: 100px; font-weight: 400;
  }
  .series-subtitle {
    position: absolute; top: 162px; left: 0; width: 100%; text-align: center;
    font-family: "Alegreya", serif; font-weight: 700; font-size: 31px; color: var(--orange);
  }
  .church-name {
    position: absolute; top: 290px; left: 0; width: 100%;
    display: flex; justify-content: center; align-items: center; gap: 10px;
    font-family: "Roboto Condensed", sans-serif; font-size: 22px; color: var(--white);
  }
  .church-name .dot { width: 16px; height: 16px; border-radius: 50%; background: var(--orange); }
  .mission {
    position: absolute; top: 400px; left: 0; width: 100%; text-align: center;
    font-family: "Alegreya", serif; font-size: 23px;
  }

  /* Back */
  .card-back { top: 638px; background: var(--royal); }
  .photo {
    position: absolute; left: 260px; top: 0; width: 334px; height: 360px;
    background: radial-gradient(ellipse at 50% 22%, var(--photo-light) 0%, var(--photo-mid) 45%, var(--photo-dark) 100%);
  }
  .back-shapes { position: absolute; inset: 0; }
  .event-title {
    position: absolute; left: 24px; top: 14px; width: 236px;
    font-family: "Satisfy", cursive; font-weight: 400; font-size: 30px; line-height: 54px;
    color: var(--gold); white-space: nowrap;
  }
  .event-date {
    position: absolute; left: 24px; top: 139px;
    font-family: "Crimson Pro", serif; font-weight: 700; font-size: 23px; color: var(--white);
  }
  .features-heading {
    position: absolute; left: 24px; top: 185px;
    font-family: "Crimson Pro", serif; font-weight: 600; font-size: 19px; color: var(--white);
  }
  .feature-list {
    position: absolute; left: 24px; top: 218px; width: 240px; list-style: none;
    font-family: "Crimson Pro", serif; font-weight: 600; font-size: 15px; line-height: 15px; color: var(--white);
  }
  .feature-list li { position: relative; padding-left: 21px; margin-bottom: 10px; }
  .feature-list li::before { content: "\2713"; position: absolute; left: 0; top: 0; }

  .photo-church-name {
    position: absolute; left: 392px; top: 92px; width: 200px;
    display: flex; justify-content: center; align-items: center; gap: 8px;
    font-family: "Roboto Condensed", sans-serif; font-size: 15px; color: var(--navy-deep);
  }
  .photo-church-name .dot { width: 12px; height: 12px; border-radius: 50%; background: var(--purple); }

  .address {
    position: absolute; right: 20px; top: 364px; text-align: right; font-style: normal;
    font-family: "Crimson Pro", serif; font-size: 14px; line-height: 17px; color: var(--white);
  }
  .address .icon { position: absolute; left: -20px; top: 2px; }
  .contact-line {
    position: absolute; right: 20px; top: 436px; display: flex; gap: 14px;
    font-family: "Crimson Pro", serif; font-size: 13px; color: var(--white);
  }
  .contact-item { display: flex; align-items: center; gap: 5px; }
  .icon { width: 12px; height: 12px; fill: var(--white); flex: none; }
</style>
</head>
<body>

<section class="card card-front">
  <span class="bracket tl"></span><span class="bracket tr"></span>
  <span class="bracket bl"></span><span class="bracket br"></span>
  <h1 class="series-title">Harbor Lanterns</h1>
  <p class="series-subtitle">What’s keeping you from God?</p>
  <p class="church-name"><span class="dot"></span>Cedar Hollow Family Church</p>
  <p class="mission">Connecting Young Families to Christ</p>
</section>

<section class="card card-back">
  <div class="photo" role="img" aria-label="Warm backlit photo of a family with raised hands standing before a glowing cross"></div>
  <svg class="back-shapes" viewBox="0 0 594 466" width="594" height="466">
    <path class="info-panel" d="M0,0 L280,0 C440,92 440,282 0,430 Z" fill="#0a56a8"/>
    <path d="M272,0 C430,90 440,270 0,418" fill="none" stroke="#ffffff" stroke-width="6"/>
    <path d="M286,0 C450,95 450,290 0,440" fill="none" stroke="#7a2a86" stroke-width="16"/>
    <path d="M0,466 C190,375 420,335 594,348 L594,466 Z" fill="#0a6cc0"/>
    <path d="M0,466 C190,375 420,335 594,348" fill="none" stroke="#ffffff" stroke-width="4"/>
    <path d="M20,466 C200,355 430,318 594,332" fill="none" stroke="#f28c1c" stroke-width="7"/>
  </svg>

  <h2 class="event-title">Westbrook Commons<br>Open Day...</h2>
  <p class="event-date">Date: Sept 23rd @ 10:30</p>
  <p class="features-heading">Features of the event:</p>
  <ul class="feature-list">
    <li>Free lunch</li>
    <li>Children’s program</li>
    <li>Bouncy Castle</li>
    <li>Start of the “Harbor Lanterns” messages.</li>
    <li>Sample of topics</li>
  </ul>

  <p class="photo-church-name"><span class="dot"></span>Cedar Hollow Family Church</p>

  <address class="address">
    <svg class="icon" viewBox="0 0 24 24"><path d="M12 2a7 7 0 0 0-7 7c0 5 7 13 7 13s7-8 7-13a7 7 0 0 0-7-7zm0 9.5A2.5 2.5 0 1 1 12 6.5a2.5 2.5 0 0 1 0 5z"/></svg>
    1875 Maple Ridge Road<br>Lakeview<br>ON L3X 2P4 Canada
  </address>

  <div class="contact-line">
    <span class="contact-item"><svg class="icon" viewBox="0 0 24 24"><path d="M6.6 10.8a15 15 0 0 0 6.6 6.6l2.2-2.2a1 1 0 0 1 1-.25 11.4 11.4 0 0 0 3.6.57 1 1 0 0 1 1 1V20a1 1 0 0 1-1 1A17 17 0 0 1 3 4a1 1 0 0 1 1-1h3.5a1 1 0 0 1 1 1c0 1.25.2 2.45.57 3.57a1 1 0 0 1-.25 1z"/></svg>555.214.0390</span>
    <span class="contact-item"><svg class="icon" viewBox="0 0 24 24"><path d="M2 5h20v14H2z M2 5l10 8 10-8" fill="none" stroke="#fff" stroke-width="2"/></svg>hello@cedarhollowchurch.ca</span>
    <span class="contact-item"><svg class="icon" viewBox="0 0 24 24"><circle cx="12" cy="12" r="9" fill="none" stroke="#fff" stroke-width="2"/><path d="M3 12h18M12 3c3 3 3 15 0 18M12 3c-3 3-3 15 0 18" fill="none" stroke="#fff" stroke-width="1.6"/></svg>www.cedarhollowchurch.ca</span>
  </div>
</section>

</body>
</html>
```